Webdesign für islamisches Bestattungsunternehmen
Zielgruppe
islamisches Bestattungsunternehmen, Grabsteine, Grabpflege
Aufgabenstellung
wir wollen ein elegantes design mit einem hauch an exklusivität. wir sind nicht auf billig aus, tatsächlich hochwertig, etwas teurer als die konkurrenz aber dafür bieten wir auch was an.
unser logo haben wir auch hier machen lassen.
www.nur-samira.eu
LEUTE!
Wir wünschen uns dass direkt auf der ersten seite die 3 optionen sofort ersichtlich sind!!! nicht dass die leute noch runterscrollen müssen...

```html
<!DOCTYPE html>
<html lang="de">
<head>
<meta charset="utf-8">
<title>Nur-Samira – Islamische Bestattungen</title>
<link href="https://fonts.googleapis.com/css2?family=Cinzel:wght@400;600;700&family=Source+Sans+3:ital,wght@0,400;0,600;1,400&display=swap" rel="stylesheet">
<style>
:root{
  --bg:#000;
  --gold:#d2b35f;
  --gold-soft:#b99a4c;
  --text:#e9e2cf;
  --panel:#111;
  --band:#2a2a2a;
  --footer:#1c1c1c;
  --line:#3a3a3a;
}
*{margin:0;padding:0;box-sizing:border-box}
html,body{width:1200px;height:2809px;overflow:hidden;background:var(--bg)}
body{position:relative;font-family:"Source Sans 3",sans-serif;color:var(--text)}
.abs{position:absolute}
.serif{font-family:"Cinzel",serif}
.gold{color:var(--gold)}
.btn{position:absolute;border:1.5px solid var(--gold);color:var(--gold);font-family:"Cinzel",serif;font-weight:700;font-size:11px;display:flex;align-items:center;justify-content:center}

/* header */
.topbar{top:14px;left:130px;right:130px;height:16px;font-size:8px;color:var(--text);display:flex;justify-content:space-between;align-items:center}
.topbar span{display:flex;align-items:center;gap:6px}
.brand{top:30px;left:500px;width:200px;text-align:center;font-family:"Cinzel",serif;font-weight:700;font-size:13px;color:var(--gold);letter-spacing:.5px}
.brand i{display:block;width:16px;height:16px;border-radius:50%;background:var(--gold);margin:0 auto 3px}
.nav{top:70px;left:0;width:1200px;display:flex;justify-content:center;gap:40px;font-size:9px;letter-spacing:.5px}
.nav a{color:var(--text);text-decoration:none;padding-bottom:4px}
.nav a.active{border-bottom:1px solid var(--gold)}

/* hero */
.hero-photo{top:135px;left:160px;width:879px;height:390px;border-radius:140px 140px 0 0/60px 60px 0 0;background:linear-gradient(180deg,#2b2624 0%,#3a1e1e 40%,#241a16 75%,#050505 100%)}
.hero-kicker{top:182px;width:1200px;text-align:center;font-family:"Cinzel",serif;font-size:10px;color:var(--gold)}
.hero-title{top:205px;width:1200px;text-align:center;font-family:"Cinzel",serif;font-weight:700;font-size:31px;line-height:43px;color:var(--gold)}
.dots{top:378px;left:582px;display:flex;gap:8px;align-items:center}
.dots i{width:5px;height:5px;border-radius:50%;background:var(--gold-soft)}
.dots i.on{width:9px;height:9px;background:var(--gold)}
.card{top:415px;width:203px;height:123px;background:var(--panel)}
.card h3{position:absolute;top:22px;left:22px;font-family:"Cinzel",serif;font-weight:400;font-size:18px;line-height:22px;color:var(--gold)}
.card .more{position:absolute;left:0;bottom:0;width:100%;height:41px;background:var(--band);font-family:"Cinzel",serif;font-size:11px;color:var(--gold-soft);padding:16px 24px}
.card .art{position:absolute;right:0;bottom:0;width:74px;height:86px;background:linear-gradient(160deg,#c9a955,#8c7033);opacity:.9}

/* about */
.about-title{top:655px;left:265px;font-family:"Cinzel",serif;font-size:22px;line-height:27px;color:var(--gold)}
.about-text{top:752px;left:265px;width:240px;font-size:9.5px;line-height:15px}
.hours{left:265px;font-family:"Cinzel",serif;font-size:9.5px}
.ornament{background:radial-gradient(circle,#1a160e 0%,#120f09 55%,transparent 72%)}
.photo-back{top:651px;left:767px;width:185px;height:237px;background:linear-gradient(160deg,#5a5a4e,#2a2a24 60%,#111)}
.photo-front{top:699px;left:625px;width:211px;height:237px;border:1px solid var(--gold);background:linear-gradient(150deg,#4a4a46,#1c1c1c 55%,#0c0c0c)}

/* testimonial */
.quote-kicker{top:1047px;width:1200px;text-align:center;font-family:"Cinzel",serif;font-size:9px;letter-spacing:2.5px;color:var(--gold)}
.quote-title{top:1067px;width:1200px;text-align:center;font-family:"Cinzel",serif;font-size:21px;color:var(--gold)}
.quote-text{top:1122px;left:390px;width:420px;text-align:center;font-style:italic;font-size:11px;line-height:22.5px;color:var(--gold)}
.quote-name{top:1212px;width:1200px;text-align:center;font-size:11px;line-height:15px;color:var(--gold)}

/* products */
.shop-kicker{top:1320px;width:1200px;text-align:center;font-family:"Cinzel",serif;font-size:10px;letter-spacing:2.5px;color:var(--text)}
.shop-title{top:1340px;width:1200px;text-align:center;font-family:"Cinzel",serif;font-size:23px;color:var(--gold)}
.grid{top:1393px;left:228px;width:741px;height:434px;display:grid;grid-template-columns:repeat(6,1fr);grid-template-rows:repeat(3,1fr);gap:2px}
.grid div{background:linear-gradient(170deg,#4a4a48,#2a2a28 60%,#1e1f1c)}
.grid div:nth-child(odd){background:linear-gradient(170deg,#3c3d3a,#252622 60%,#2f2f2a)}
.shop-cta{top:1561px;left:402px;width:395px;height:94px;background:#111;box-shadow:0 0 12px #000}
.shop-cta div{position:absolute;inset:6px;border:1px dashed var(--gold);display:flex;align-items:center;justify-content:center;text-align:center;font-family:"Cinzel",serif;font-size:20px;line-height:31px;color:var(--gold)}

/* contact */
.director{top:2053px;left:272px;width:202px;height:283px;border-radius:0 16px 0 16px;border:1px solid var(--gold);background:linear-gradient(180deg,#5c7a48 0%,#3f4e35 35%,#1e1f1e 60%,#151515)}
.director-role{top:2352px;left:230px;width:285px;text-align:center;font-family:"Cinzel",serif;font-size:15px;font-weight:600;color:var(--gold)}
.director-name{top:2389px;left:230px;width:285px;text-align:center;font-size:10.5px;line-height:17px}
.git-title{top:2008px;left:631px;font-family:"Cinzel",serif;font-size:22px;color:var(--gold)}
.info-h{font-family:"Cinzel",serif;font-weight:700;font-size:14px;color:var(--gold);display:flex;align-items:center;gap:6px}
.info-p{font-family:"Cinzel",serif;font-size:9px;line-height:12px;color:var(--gold-soft)}
.field{border-bottom:1px solid var(--gold);font-size:10.5px;padding-left:16px}

/* footer */
.footer{top:2506px;left:0;width:1200px;height:303px;background:var(--footer)}
.footer-claim{top:2597px;left:129px;font-family:"Cinzel",serif;font-size:29px;line-height:36px;color:var(--gold-soft)}
.fh{font-family:"Cinzel",serif;font-size:15px;color:var(--gold-soft)}
.fp{font-family:"Cinzel",serif;font-size:14px;line-height:18px;color:var(--gold-soft)}
.footer-rule{top:2740px;left:130px;width:938px;height:1px;background:var(--line)}
.footer-nav{top:2770px;left:154px;display:flex;gap:38px;font-family:"Cinzel",serif;font-size:11px;color:var(--gold-soft)}
.copyright{top:2770px;right:133px;font-size:9.5px;color:var(--gold-soft)}
</style>
</head>
<body>

<header>
  <div class="abs topbar">
    <span><svg width="9" height="9" viewBox="0 0 10 10"><circle cx="5" cy="5" r="4" fill="none" stroke="#e9e2cf"/><path d="M5 2.5V5h2" stroke="#e9e2cf" fill="none"/></svg>Mon - Fri 8:00 - 18:00 / Sunday 8:00 - 14:00</span>
    <span><svg width="9" height="9" viewBox="0 0 10 10"><path d="M2 1l2 2-1 1.5c.6 1.2 1.4 2 2.5 2.5L7 6l2 2-1.5 1.5C4.5 9 1 5.5.5 2.5z" fill="#e9e2cf"/></svg>0176/30581146</span>
  </div>
  <div class="abs brand"><i></i>Nur-Samira</div>
  <nav class="abs nav">
    <a class="active">HOME</a><a>SERVICES</a><a>MEMORIALS</a><a>PAGES</a><a>CONTACTS</a>
  </nav>
</header>

<section class="hero">
  <div class="abs hero-photo" role="img" aria-label="Trauerhalle mit roten und weißen Blumengestecken und schwarzem Tuch"></div>
  <svg class="abs" style="top:55px;left:0" width="1200" height="170" viewBox="0 0 1200 170">
    <path d="M132 165 C132 90 220 75 330 75 L355 53 L565 53 M635 53 L845 53 L870 75 C980 75 1068 90 1068 165" fill="none" stroke="#d2b35f" stroke-width="1.2"/>
  </svg>
  <div class="abs hero-kicker">BESTATTUNGSINSTITUTE</div>
  <h1 class="abs hero-title">FAMILIEN HELFEN, SICH ZU VERBINDEN,<br>EHRE &amp; ERINNERE DICH</h1>
  <div class="btn" style="top:323px;left:546px;width:107px;height:34px">Get In Touch</div>
  <div class="abs dots"><i></i><i class="on"></i><i></i></div>

  <div class="abs card" style="left:249px"><h3>Bestattung<br>Leistungen</h3><div class="more">More Info</div><div class="art" role="img" aria-label="Goldene Rosen"></div></div>
  <div class="abs card" style="left:499px"><h3>Grabsteine<br>Leistungen</h3><div class="more">More Info</div><div class="art" role="img" aria-label="Goldener Grabstein"></div></div>
  <div class="abs card" style="left:750px"><h3>Grabpflege<br>Leistungen</h3><div class="more">More Info</div><div class="art" role="img" aria-label="Goldene Grablaterne"></div></div>
</section>

<section class="about">
  <h2 class="abs about-title">Wir helfen Familien,<br>den letzten Abschied<br>zu nehmen</h2>
  <p class="abs about-text">Wir wissen Ihr Vertrauen sehr zu schätzen. Unsere Kunden wählen uns und unsere Produkte, weil sie wissen, dass wir die Besten sind.</p>
  <p class="abs hours" style="top:815px">MON-FRI: 9 AM – 22 PM</p>
  <p class="abs hours" style="top:839px">SATURDAY: 9 AM – 20 PM</p>
  <div class="btn" style="top:884px;left:264px;width:108px;height:35px;font-weight:400">About Us</div>
  <div class="abs ornament" role="img" aria-label="Goldenes Mandala-Ornament" style="top:600px;left:720px;width:310px;height:340px"></div>
  <div class="abs photo-back" role="img" aria-label="Trauernde Frau am Friedhof"></div>
  <div class="abs photo-front" role="img" aria-label="Tröstende Umarmung in schwarzer Kleidung"></div>
</section>

<section class="testimonial">
  <svg class="abs" style="top:1005px;left:310px" width="580" height="270" viewBox="0 0 580 270">
    <path d="M98 4 H482 C510 4 505 44 540 60 C570 80 575 120 582 134 C575 148 570 190 540 210 C505 226 510 266 482 266 H98 C70 266 75 226 40 210 C10 190 5 148 -2 134 C5 120 10 80 40 60 C75 44 70 4 98 4Z" fill="#000" stroke="#d2b35f" stroke-width="1.2" transform="translate(6 0) scale(.98 1)"/>
    <path d="M54 135h18M54 135l5-4M54 135l5 4M526 135h-18M526 135l-5-4M526 135l-5 4" stroke="#e9e2cf" stroke-width="1.3" fill="none"/>
    <path d="M272 195h36" stroke="#d2b35f"/>
  </svg>
  <p class="abs quote-kicker">REFERENZEN</p>
  <h2 class="abs quote-title">Was unsere Familien sagen</h2>
  <p class="abs" style="top:1097px;width:1200px;text-align:center;font-family:'Cinzel',serif;font-weight:700;font-size:18px;color:var(--gold)">”</p>
  <p class="abs quote-text">When it comes to immediate problem solving with such delicate and sometimes terrifying circumstances, you know you have Nur-Samira Service to fully trust and rely on. Thank you for your impeccable work!</p>
  <p class="abs quote-name">KARIM HADDAD<br>Manager</p>
</section>

<section class="products">
  <p class="abs shop-kicker">UNSER LADEN</p>
  <h2 class="abs shop-title">Unsere Produkte</h2>
  <div class="abs ornament" role="img" aria-label="Goldenes Ornament links" style="top:1450px;left:105px;width:240px;height:320px"></div>
  <div class="abs ornament" role="img" aria-label="Goldenes Ornament rechts" style="top:1450px;left:855px;width:240px;height:320px"></div>
  <div class="abs grid" role="img" aria-label="Fotogalerie mit Grabsteinen und Grabanlagen">
    <div></div><div></div><div></div><div></div><div></div><div></div>
    <div></div><div></div><div></div><div></div><div></div><div></div>
    <div></div><div></div><div></div><div></div><div></div><div></div>
  </div>
  <div class="abs shop-cta"><div>Möchten Sie einen Grabstein<br>für Ihre Lieben kaufen</div></div>
  <div class="btn" style="top:1856px;left:546px;width:107px;height:35px">View All</div>
</section>

<section class="contact">
  <div class="abs director" role="img" aria-label="Porträt des Geschäftsführers im schwarzen Hemd"></div>
  <p class="abs director-role">MANAGING DIRECTOR</p>
  <svg class="abs" style="top:2376px;left:316px" width="110" height="6"><path d="M0 3h110" stroke="#b5603a" stroke-width=".8"/><circle cx="55" cy="3" r="2.5" fill="#d2b35f"/></svg>
  <p class="abs director-name">Name sample<br>Name</p>

  <h2 class="abs git-title">Get In Touch</h2>
  <div class="abs info-h" style="top:2060px;left:633px"><svg width="14" height="18" viewBox="0 0 14 18"><path d="M7 0a7 7 0 0 1 7 7c0 5-7 11-7 11S0 12 0 7a7 7 0 0 1 7-7z" fill="#d2b35f"/><circle cx="7" cy="7" r="2.6" fill="#000"/></svg>Address</div>
  <p class="abs info-p" style="top:2092px;left:631px">Germany —<br>12 Lindenallee, Büro 4<br>Berlin, DE 10115</p>
  <div class="abs info-h" style="top:2060px;left:810px"><svg width="22" height="15" viewBox="0 0 22 15"><rect width="22" height="15" fill="#d2b35f"/><path d="M0 0l11 8 11-8M0 15l8-8M22 15l-8-8" stroke="#000" fill="none"/></svg>Contact</div>
  <p class="abs info-p" style="top:2092px;left:812px">E-Mail: kontobe74@nur-samira.eu<br><br>Tel.: 0176/30581146</p>
  <p class="abs info-h" style="top:2166px;left:631px">Have a question?</p>
  <div class="abs field" style="top:2207px;left:632px;width:140px;height:26px">Vorname</div>
  <div class="abs field" style="top:2207px;left:810px;width:138px;height:26px">Email</div>
  <div class="abs field" style="top:2272px;left:632px;width:316px;height:64px">Message</div>
  <div class="abs" style="top:2363px;left:632px;width:71px;height:30px;border:1.5px solid var(--gold);color:var(--gold);font-family:'Cinzel',serif;font-size:12px;display:flex;align-items:center;justify-content:center">SEND</div>
</section>

<footer>
  <div class="abs footer"></div>
  <p class="abs footer-claim">Wir organisieren &amp;<br>gestalten Zeremonien.</p>
  <p class="abs fh" style="top:2578px;left:627px">Address</p>
  <p class="abs fp" style="top:2611px;left:627px">Germany —<br>12 Lindenallee, Büro 4<br>Berlin, DE 10115</p>
  <p class="abs fh" style="top:2578px;left:872px">Say Hello</p>
  <p class="abs fp" style="top:2611px;left:872px">E-Mail: kontobe74@nur-samira.eu<br><br>Tel.: 0176/30581146</p>
  <div class="abs footer-rule"></div>
  <nav class="abs footer-nav"><span>Home</span><span>Our Services</span><span>Our Pricing</span><span>Shop</span><span>Contact Us</span></nav>
  <p class="abs copyright">Copyright Nur-Samira.eu © 2021</p>
</footer>

</body>
</html>
```